Bright, Fun and hard to forget home inspection business card.

We need a Business card design for a new Home Inspection company. We are building a brand that is bright, fun and easy to remember.

Target Market(s)

Anyone involed in buying and selling of homes.

Industry/Entity Type

Home Inspection

Contact Information for Business Card

Colin Marlowe Owner/Inspector

Wedsite- PorchAndRafterCheck.example
Phone: 253-555-0187
Email- ColinMarlowe@mailbox.example
WA Lic # 4806

Requirements
Must have
• BRQV LOGO somewhere on card.

```html
<!DOCTYPE html>
<html lang="en">
<head>
<meta charset="utf-8">
<title>Porch and Rafter Check – Business Card</title>
<link rel="stylesheet" href="https://fonts.googleapis.com/css2?family=Open+Sans:wght@400;600&display=swap">
<style>
  :root {
    --page-bg: #e9e7e5;
    --card-orange: #e9623f;
    --card-edge: #d9532f;
    --name-grey: #e3d6d0;
    --title-dark: #3b2620;
    --detail-light: #f2d8cc;
    --logo-white: #ffffff;
  }
  * { margin: 0; padding: 0; box-sizing: border-box; }
  html, body {
    width: 1200px;
    height: 970px;
    overflow: hidden;
    background: var(--page-bg);
    font-family: "Open Sans", Arial, sans-serif;
  }
  .business-card {
    position: absolute;
    left: 150px;
    top: 235px;
    width: 900px;
    height: 500px;
    border-radius: 28px;
    background: var(--card-orange);
    box-shadow: inset 0 0 0 2px var(--card-edge);
  }
  .contact-block {
    position: absolute;
    left: 44px;
    top: 240px;
  }
  .person-name {
    font-size: 27px;
    font-weight: 600;
    letter-spacing: 0.5px;
    color: var(--name-grey);
    text-transform: uppercase;
    line-height: 1.1;
  }
  .person-title {
    font-size: 19px;
    font-weight: 400;
    color: var(--title-dark);
    margin-top: 2px;
  }
  .detail-list {
    list-style: none;
    margin-top: 42px;
  }
  .detail-list li {
    display: flex;
    align-items: center;
    gap: 10px;
    font-size: 19px;
    color: var(--detail-light);
    line-height: 30px;
  }
  .detail-list svg {
    width: 16px;
    height: 16px;
    fill: var(--detail-light);
    flex: none;
  }
  .licence { padding-left: 0; }
  .brand-mark {
    position: absolute;
    left: 530px;
    top: 70px;
    width: 320px;
    display: flex;
    align-items: flex-start;
    gap: 18px;
  }
  .brand-square {
    width: 44px;
    height: 44px;
    background: var(--logo-white);
    flex: none;
    margin-top: 12px;
  }
  .brand-name {
    font-size: 46px;
    font-weight: 600;
    line-height: 1.08;
    color: var(--logo-white);
    text-transform: uppercase;
  }
</style>
</head>
<body>
  <div class="business-card">
    <div class="brand-mark">
      <span class="brand-square"></span>
      <div class="brand-name">Porch<br>and Rafter<br>Check<br>LLC</div>
    </div>

    <div class="contact-block">
      <div class="person-name">Colin Marlowe</div>
      <div class="person-title">Owner/Inspector</div>
      <ul class="detail-list">
        <li class="licence">WA Lic # 4806</li>
        <li>
          <svg viewBox="0 0 16 16" aria-hidden="true"><path d="M3.6 1.2l2.3 2.6-1.3 1.9c.9 2 2.3 3.5 4.4 4.6l1.9-1.3 2.6 2.3-1.4 2.6C6.9 13.5 2.3 8.9 1 3z"/></svg>
          253-555-0187
        </li>
        <li>
          <svg viewBox="0 0 16 16" aria-hidden="true"><path d="M1 3h14v1.2L8 8.6 1 4.2z"/><path d="M1 5.6l7 4.4 7-4.4V13H1z"/></svg>
          ColinMarlowe@mailbox.example
        </li>
        <li>
          <svg viewBox="0 0 16 16" aria-hidden="true"><circle cx="8" cy="8" r="6.3" fill="none" stroke="#f2d8cc" stroke-width="1.4"/><ellipse cx="8" cy="8" rx="2.6" ry="6.3" fill="none" stroke="#f2d8cc" stroke-width="1.2"/><path d="M1.7 8h12.6" stroke="#f2d8cc" stroke-width="1.2"/></svg>
          PorchAndRafterCheck.example
        </li>
      </ul>
    </div>
  </div>
</body>
</html>
```